Pain Seminar Flyer 8.5x11

We are having a FREE seminar on Pain for our Bootcamp members at our gym. We are looking for a great looking flyer with pictures and a design to draw people in. I have attached our logo, pictures of the 2 speakers and a Word document of the flyer information needed. PLEASE PLEASE make our head shots small and in a circle like the example flyer we attached but obviously make the flyer much much nicer than the example. Also we attached pic ideas about pain.
- This must be in PSD. format WITH LAYERS and fonts so we can edit the time or reuse the flyer.
- Size 8.5x11
- Attached info. with pics and logo (along with other pics of pain!)
Thank you!
Gym

```html
<!DOCTYPE html>
<html lang="en">
<head>
<meta charset="utf-8">
<title>Free Pain Seminar Flyer</title>
<link href="https://fonts.googleapis.com/css2?family=Roboto:wght@300;400;500;700;900&display=swap" rel="stylesheet">
<style>
  :root {
    --page-bg: #e4e5e8;
    --paper: #ffffff;
    --panel: #eef0f1;
    --info-box: #c9cacc;
    --blue: #0a76c4;
    --blue-dark: #0763a6;
    --orange: #f28a1c;
    --orange-deep: #e2531f;
    --ink: #333436;
    --white: #ffffff;
  }
  * { box-sizing: border-box; margin: 0; padding: 0; }
  html, body { width: 969px; height: 1200px; overflow: hidden; }
  body {
    background: var(--page-bg);
    font-family: "Roboto", Arial, sans-serif;
    position: relative;
  }
  .flyer {
    position: absolute;
    left: 62px;
    top: 16px;
    width: 625px;
    height: 865px;
    transform: scale(1.35);
    transform-origin: top left;
    background: var(--paper);
    box-shadow: 0 6px 18px rgba(0,0,0,0.25);
    overflow: hidden;
  }
  .flyer > * { position: absolute; }
  .panel { left: 14px; top: 16px; width: 597px; height: 600px; background: var(--panel); }
  .band-orange { left: 0; top: 607px; width: 625px; height: 175px; background: linear-gradient(180deg, #f07e1c, var(--orange)); }
  .band-blue { left: 0; top: 782px; width: 625px; height: 83px; background: var(--blue); }
  .notch { left: 304px; top: 606px; }

  .headline-parts {
    right: 401px; top: 72px;
    text-align: right;
    color: var(--blue);
    font-weight: 900;
    font-size: 33px;
    line-height: 31.5px;
    letter-spacing: -0.5px;
  }
  .headline-pain {
    left: 234px; top: 46px;
    font-weight: 900;
    font-size: 132px;
    line-height: 1;
    letter-spacing: -3px;
    background: linear-gradient(180deg, var(--orange-deep), var(--orange));
    -webkit-background-clip: text;
    background-clip: text;
    color: transparent;
  }

  .ribbon { display: flex; align-items: center; justify-content: center; color: var(--white); }
  .ribbon-blue {
    left: 147px; top: 207px; width: 340px; height: 55px;
    background: var(--blue);
    clip-path: polygon(3% 0, 100% 0, 97% 100%, 0 100%);
    font-weight: 700; font-size: 38px;
  }
  .ribbon-orange {
    left: 93px; top: 261px; width: 444px; height: 54px;
    background: linear-gradient(180deg, #f4931f, var(--orange));
    clip-path: polygon(2% 0, 100% 0, 98% 100%, 0 100%);
    font-weight: 300; font-size: 35px;
    box-shadow: 0 3px 4px rgba(0,0,0,0.2);
  }

  .info-box {
    left: 44px; top: 346px; width: 539px; height: 156px;
    background: var(--info-box);
    border-radius: 12px;
    color: var(--ink);
    font-size: 12.3px;
    line-height: 16px;
  }
  .info-box > * { position: absolute; }
  .info-left { left: 34px; top: 24px; width: 200px; }
  .info-right { left: 250px; top: 24px; width: 280px; }
  .divider { left: 224px; top: 18px; height: 122px; border-left: 2px dotted #8d8e90; }
  .info-box strong { font-weight: 700; }
  .gap { display: block; height: 16px; }
  .topics { list-style: none; }
  .topics li::before { content: "\2022\00a0"; }

  .speaker-photo {
    width: 132px; height: 132px; top: 527px;
    border-radius: 50%;
    border: 3px solid var(--blue);
    background-clip: content-box;
    padding: 4px;
    background-color: var(--white);
  }
  .speaker-photo .fill { width: 100%; height: 100%; border-radius: 50%; }
  .photo-one { left: 112px; }
  .photo-one .fill { background: radial-gradient(circle at 50% 40%, #d8c6ad, #6d7a55 75%); }
  .photo-two { left: 370px; }
  .photo-two .fill { background: radial-gradient(circle at 50% 40%, #c99a7e, #d9d9d6 75%); }

  .name-tag {
    top: 678px; height: 22px;
    background: var(--blue);
    color: var(--white);
    font-size: 12px;
    display: flex; align-items: center; justify-content: center;
    clip-path: polygon(0 0, 100% 0, 96% 50%, 100% 100%, 0 100%, 4% 50%);
  }
  .name-tag b { font-weight: 700; margin-right: 3px; }
  .name-one { left: 72px; width: 211px; }
  .name-two { left: 330px; width: 215px; }

  .brand {
    left: 0; width: 625px; top: 740px;
    display: flex; align-items: center; justify-content: center; gap: 10px;
    color: var(--white);
    font-weight: 900; font-size: 30px; letter-spacing: 1px;
  }
  .brand-square { width: 22px; height: 22px; background: var(--white); }

  .website {
    left: 0; width: 625px; top: 834px;
    text-align: center; color: var(--white);
    font-size: 16px; letter-spacing: 1.6px;
  }
</style>
</head>
<body>
  <main class="flyer">
    <div class="panel"></div>
    <div class="band-orange"></div>
    <div class="band-blue"></div>
    <svg class="notch" width="18" height="10" viewBox="0 0 18 10"><polygon points="0,0 18,0 9,9" fill="#eef0f1"/></svg>

    <h1 class="headline-parts">BACK<br>SHOULDER<br>KNEE</h1>
    <div class="headline-pain">PAIN?</div>

    <div class="ribbon ribbon-blue">FREE SEMINAR</div>
    <div class="ribbon ribbon-orange">ON HOW TO STOP PAIN</div>

    <section class="info-box">
      <div class="info-left">
        RESERVATIONS REQUIRED.<br>
        <strong>CALL 555-014-2290 TODAY</strong><br>
        LIMITED SPACE SO DON'T<br>
        WAIT TO SIGN UP
        <span class="gap"></span>
        <strong>THURSDAY, APRIL 13th<br>7:30PM-9PM</strong>
      </div>
      <div class="divider"></div>
      <div class="info-right">
        <ul class="topics">
          <li>How to Get Out of Pain</li>
          <li>What to do When an Exercise Hurts</li>
          <li>How Exercise Helps Pain</li>
          <li>Q &amp; A to Fine Extraordinary Health</li>
        </ul>
        <span class="gap"></span>
        <strong>CORESTRIDE PERSONAL TRAINING STUDIO</strong><br>
        18 W. Elm St. Fairview, CO 80000
      </div>
    </section>

    <div class="speaker-photo photo-one"><div class="fill" role="img" aria-label="Circular head shot of speaker Daniel Marsh"></div></div>
    <div class="speaker-photo photo-two"><div class="fill" role="img" aria-label="Circular head shot of speaker Trevor Hale"></div></div>

    <div class="name-tag name-one"><b>Daniel Marsh,</b> PT, DPT, OCS</div>
    <div class="name-tag name-two"><b>Trevor Hale,</b> MS, CSCS, FMS</div>

    <div class="brand"><span class="brand-square"></span>CORESTRIDE BOOTCAMPS</div>
    <div class="website">www.corestridefit.com</div>
  </main>
</body>
</html>
```